Simple, bright, clean website - 3 pages, easy to update with WordPress!

I want to update my website (brelvatix.com) with a brighter/cleaner interface. It is quite dark right now. I would like it to be similar to a partner site (https://www.nodavent-44.com/). White with some orange highlights (matching the logo). I want to be able to easily update the site content. There should be 3 main pages: About, Services, Contact. I also like a design similar to quorfen.com

Target Market(s)

Anyone using technology to achieve business goals.

Industry/Entity Type

Managed Service Provider (IT)

Coding

Coded - Design and coding required

Number of Pages Required

3 page

Colors
F0912C
F2A743
F7CA91
FBE8D2
FDF5EE

Requirements
Must have
• Links to standard social media apps like WorkLattice, Pallgrove, etc.. Easy to edit and add pages.

```html
<!DOCTYPE html>
<html lang="en">
<head>
<meta charset="utf-8">
<title>Brelvatix Consulting</title>
<link rel="stylesheet" href="https://fonts.googleapis.com/css2?family=Montserrat:wght@800&family=Roboto:wght@300;400;500;700&display=swap">
<style>
:root{
  --orange:#f7a100;
  --orange-deep:#f0912c;
  --orange-soft:#f7ca91;
  --cream:#fdf5ee;
  --gray:#5e5e5e;
  --gray-dark:#3a3a3a;
  --ink:#1f1f1f;
  --text:#555;
  --white:#fff;
}
*{box-sizing:border-box;margin:0;padding:0}
html,body{width:1200px;height:2754px;overflow:hidden;background:var(--white)}
body{font-family:"Roboto",Arial,sans-serif;color:var(--ink)}
.page{position:relative;width:1200px;height:2754px;overflow:hidden}
.abs{position:absolute}
.btn{position:absolute;display:flex;align-items:center;justify-content:center;background:var(--orange);color:var(--white);font:500 16px "Roboto",Arial,sans-serif;border-radius:24px;text-decoration:none}
.heading{font-family:"Montserrat",Arial,sans-serif;font-weight:800;letter-spacing:-0.5px}

/* header */
.site-header{position:absolute;left:0;top:0;width:1200px;height:97px;background:var(--white);z-index:5}
.brand{position:absolute;display:flex;align-items:center;gap:10px;color:#8a8a8a;font:300 46px "Roboto",Arial,sans-serif;letter-spacing:1px}
.brand-dot{width:14px;height:14px;border-radius:50%;background:var(--orange)}
.header-brand{left:144px;top:18px}
.phone{left:718px;top:10px;display:flex;align-items:center;gap:6px;font:500 19px "Roboto",Arial,sans-serif;color:#777}
.phone-icon{width:28px;height:28px;border-radius:50%;background:#9a9a9a;display:flex;align-items:center;justify-content:center}
.main-nav a{position:absolute;top:58px;font:500 15px "Roboto",Arial,sans-serif;color:var(--ink);text-decoration:none}
.login{left:941px;top:46px;width:114px;height:43px}

/* hero */
.hero{position:absolute;left:0;top:97px;width:1200px;height:520px;background:linear-gradient(100deg,#f2f4f7 0%,#dfe4ea 35%,#8a8f98 60%,#3a3d44 80%,#2a2c31 100%)}
.hero-title{position:absolute;left:144px;top:213px;font-size:57px;line-height:68px;color:#2b2b2b;z-index:2}
.get-started{left:146px;top:369px;width:154px;height:43px;z-index:2}
.wave{position:absolute;left:0;display:block}

/* about */
.about-stem{left:332px;top:633px;width:11px;height:60px;background:var(--orange);border-radius:5px}
.about-photo{left:147px;top:688px;width:380px;height:380px;border-radius:50%;border:7px solid var(--orange);overflow:hidden;background:var(--white)}
.about-photo .fill{position:absolute;inset:8px;border-radius:50%;background:linear-gradient(140deg,#b89a74 0%,#e7e4df 40%,#7c9ec9 75%,#35527c 100%)}
.about-title{left:590px;top:660px;font-size:56px;color:#111}
.about-sub{left:590px;top:743px;font:400 16px "Roboto",Arial,sans-serif;color:#111}
.about-text{left:591px;top:783px;width:464px;font:300 14px/24.8px "Roboto",Arial,sans-serif;color:var(--text);text-align:justify}
.read-more{left:591px;top:982px;width:154px;height:43px}

/* services */
.services{position:absolute;left:0;top:1170px;width:1200px;height:745px;background:radial-gradient(ellipse at 70% 40%,#6d6d6d 0%,var(--gray) 55%,#555 100%)}
.services-title{left:0;width:1200px;top:1222px;text-align:center;font-size:54px;color:var(--white)}
.svc{position:absolute;width:216px;height:216px;border-radius:50%;overflow:hidden}
.svc .photo{position:absolute;inset:0}
.svc .label{position:absolute;left:26px;bottom:0;width:164px;height:72px;background:var(--white);border-radius:50% 50% 0 0/70% 70% 0 0;display:flex;align-items:center;justify-content:center;text-align:center;font:500 12.5px/17px "Roboto",Arial,sans-serif;color:#111;padding-bottom:6px}
.svc.active{border:5px solid var(--orange)}
.svc.active .label{background:var(--orange);color:var(--white);left:21px}

/* contact */
.contact{position:absolute;left:0;top:1900px;width:1200px;height:605px;background:linear-gradient(180deg,var(--orange) 0%,#f5a20a 50%,var(--orange) 100%)}
.contact-title{left:0;width:1200px;top:1990px;text-align:center;font-size:54px;color:var(--white)}
.field{position:absolute;height:52px;border:none;background:var(--white);padding:0 21px;font:400 16px "Roboto",Arial,sans-serif;color:#555;outline:none}
.field::placeholder{color:#555}
textarea.field{padding-top:16px;resize:none}
.submit{position:absolute;left:523px;top:2380px;width:154px;height:43px;border:none;border-radius:24px;background:var(--gray-dark);color:var(--white);font:500 16px "Roboto",Arial,sans-serif}

/* footer */
.footer-brand{left:150px;top:2570px;font-size:78px;gap:14px}
.footer-brand .brand-dot{width:22px;height:22px}
.mail-icon{left:576px;top:2566px;width:40px;height:40px;border-radius:50%;border:2px solid var(--orange);display:flex;align-items:center;justify-content:center}
.mail-text{left:631px;top:2572px;font:500 23px "Roboto",Arial,sans-serif;color:#111}
.socials{left:930px;top:2574px;display:flex;gap:12px}
.socials a{font:500 14px "Roboto",Arial,sans-serif;color:#111;text-decoration:none}
.footer-nav{left:576px;top:2630px;font:500 14px "Roboto",Arial,sans-serif;color:#111}
.footer-nav a{color:#111;text-decoration:none}
.footer-nav span{margin:0 9px}
.copyright{left:0;width:1200px;top:2703px;text-align:center;font:400 14px "Roboto",Arial,sans-serif;color:#333}
</style>
</head>
<body>
<div class="page">

  <header class="site-header">
    <div class="brand header-brand"><span class="brand-dot"></span>brelvatix</div>
    <div class="abs phone">
      <span class="phone-icon"><svg width="16" height="16" viewBox="0 0 24 24"><path fill="#fff" d="M6.6 10.8a15 15 0 0 0 6.6 6.6l2.2-2.2c.3-.3.7-.4 1-.2 1.1.4 2.3.6 3.6.6.6 0 1 .4 1 1V20c0 .6-.4 1-1 1A17 17 0 0 1 3 4c0-.6.4-1 1-1h3.5c.6 0 1 .4 1 1 0 1.3.2 2.5.6 3.6.1.3 0 .7-.2 1z"/></svg></span>
      +1 555 010 0142
    </div>
    <nav class="main-nav">
      <a style="left:539px" href="#">HOME</a>
      <a style="left:627px" href="#">ABOUT</a>
      <a style="left:721px" href="#">SERVICES</a>
      <a style="left:836px" href="#">CONTACT</a>
    </nav>
    <a class="btn login" href="#">LOGIN</a>
  </header>

  <section class="hero" role="img" aria-label="Hands holding a phone with glowing security padlock and data overlays"></section>
  <h1 class="abs heading hero-title">BRELVATIX<br>CONSULTING</h1>
  <a class="btn get-started" href="#">GET STARTED</a>
  <svg class="wave" style="top:510px" width="1200" height="110" viewBox="0 0 1200 110"><path fill="#fff" d="M0 60 C 200 100 420 110 640 85 S 1000 10 1200 25 L1200 110 L0 110Z"/></svg>

  <div class="abs about-stem"></div>
  <div class="abs about-photo"><div class="fill" role="img" aria-label="Business partners shaking hands over charts and a tablet"></div></div>
  <h2 class="abs heading about-title">ABOUT US</h2>
  <p class="abs about-sub">SIMPLIFIED IT THAT DRIVES YOUR BUSINESS FORWARD</p>
  <p class="abs about-text">Sed ut perspiciatis unde omnis iste natus error sit voluptatem accusantium doloremque laudantium, totam rem aperiam, eaque ipsa quae ab illo inventore veritatis et quasi architecto beatae vitae dicta sunt explicabo. Nemo enim ipsam voluptatem quia voluptas sit aspernatur aut odit aut fugit, sed quia consequuntur magni dolores eos qui ratione voluptatem sequi nesciunt. Neque porro quisquam est, qui dolorem ipsum quia dolor sit amet, consectetur, adipisci velit, sed quia non numquam eius modi</p>
  <a class="btn read-more" href="#">READ MORE</a>

  <section class="services" role="img" aria-label="Dark grey background of network particles and padlock icons"></section>
  <svg class="wave" style="top:1085px" width="1200" height="90" viewBox="0 0 1200 90"><path fill="#5e5e5e" d="M0 85 C 250 85 420 5 640 5 S 1000 55 1200 45 L1200 90 L0 90Z"/></svg>
  <h2 class="abs heading services-title">OUR SERVICES</h2>

  <div class="svc" style="left:146px;top:1329px"><div class="photo" role="img" aria-label="Laptop and tablet showing analytics dashboards" style="background:linear-gradient(150deg,#f1efec,#c7ccd3 55%,#7d8794)"></div><div class="label">MANAGED IT<br>SERVICES</div></div>
  <div class="svc active" style="left:377px;top:1329px"><div class="photo" role="img" aria-label="Consultants meeting in a bright office" style="background:linear-gradient(150deg,#eef1f4,#c9b8a5 50%,#4b5260)"></div><div class="label">IT<br>CONSULTING</div></div>
  <div class="svc" style="left:608px;top:1329px"><div class="photo" role="img" aria-label="Glowing blue VoIP network graphic" style="background:radial-gradient(circle at 55% 45%,#3f7fd6,#163a8c 55%,#0a1a45)"></div><div class="label">VOIP<br>SOLUTIONS</div></div>
  <div class="svc" style="left:839px;top:1329px"><div class="photo" role="img" aria-label="Cloud shape made of circuit board lights" style="background:radial-gradient(circle at 50% 40%,#3d6b73,#1c2e36 60%,#0c1418)"></div><div class="label">CLOUD<br>SERVICES</div></div>
  <div class="svc" style="left:262px;top:1562px"><div class="photo" role="img" aria-label="Keyboard with digital security padlock overlay" style="background:radial-gradient(circle at 45% 40%,#4a5ea0,#23305e 55%,#101628)"></div><div class="label">CYBERSECURITY<br>SOLUTIONS</div></div>
  <div class="svc" style="left:493px;top:1562px"><div class="photo" role="img" aria-label="Laptop with backup data cloud icons" style="background:linear-gradient(150deg,#c9cdd3,#8b9099 50%,#3c4048)"></div><div class="label">BACKUP &amp; DISASTER<br>RECOVERY</div></div>
  <div class="svc" style="left:724px;top:1562px"><div class="photo" role="img" aria-label="Hand touching a screen of office app tiles" style="background:linear-gradient(150deg,#6f8fb7,#2b4f86 55%,#132848)"></div><div class="label">MANAGED CORVEXA<br>365 SERVICES</div></div>

  <section class="contact" role="img" aria-label="Orange-tinted background of business people in silhouette"></section>
  <svg class="wave" style="top:1825px" width="1200" height="90" viewBox="0 0 1200 90"><path fill="#f7a100" d="M0 30 C 200 40 380 85 560 80 S 950 10 1200 8 L1200 90 L0 90Z"/></svg>
  <h2 class="abs heading contact-title">CONTACT</h2>
  <form>
    <input class="field" style="left:234px;top:2099px;width:359px" type="text" placeholder="First Name">
    <input class="field" style="left:605px;top:2099px;width:360px" type="text" placeholder="Last Name">
    <input class="field" style="left:234px;top:2164px;width:360px" type="email" placeholder="Email address">
    <input class="field" style="left:606px;top:2164px;width:360px" type="tel" placeholder="Phone Number">
    <textarea class="field" style="left:234px;top:2229px;width:732px;height:115px" placeholder="Message"></textarea>
    <button class="submit" type="submit">SUBMIT</button>
  </form>

  <footer>
    <div class="brand footer-brand abs"><span class="brand-dot"></span>brelvatix</div>
    <div class="abs mail-icon"><svg width="20" height="14" viewBox="0 0 20 14"><rect x="1" y="1" width="18" height="12" fill="none" stroke="#f7a100" stroke-width="2"/><path d="M1 1 L10 8 L19 1" fill="none" stroke="#f7a100" stroke-width="2"/></svg></div>
    <div class="abs mail-text">info@brelvatix.com</div>
    <div class="abs socials"><a href="#">Pallgrove</a><a href="#">Chatwave</a><a href="#">WorkLattice</a></div>
    <nav class="abs footer-nav"><a href="#">HOME</a><span>/</span><a href="#">ABOUT</a><span>/</span><a href="#">SERVICES</a><span>/</span><a href="#">CONTACT</a></nav>
    <p class="abs copyright">© 2024 Brelvatix. All rights reserved.Privacy &nbsp;|&nbsp; Terms of Use</p>
  </footer>

</div>
</body>
</html>
```